Website for "Bright Over Dusk Ltd" cleaning bsuiness

We require a website to expose our business to the local market. We want to provide background on who we are and what we do but in an easily digestible way. We clean domestic and commercial premises and want to provide a list of all of our services to potential customers. We operate out of Warrington in the UK.

We would like the website to be animated in some way so that the experience of using it is not dull or mundane. This website needs to be an extension of our company.

Target Market(s)

30 - 60 year olds for Domestic plus commercial clients

Industry/Entity Type

Cleaning Service

Coding

Coded - Design and coding required

Number of Pages Required

4 page

Font styles to use
Sans Serif

Colors
0455a3
3176b5
85acd3
cfdeed
ffffff
000000
1b1b1b
c8c8c8
757575

Requirements
Must have
• Logo which has been provided. Theme based around the logo and its colours. Simple layout to avoid confusion.
Nice to have
• Animations where possible to impress the customer.
Should not have
• any pictures of cleaning equipment, fairies, maids etc

```html
<!DOCTYPE html>
<html lang="en">
<head>
<meta charset="utf-8">
<title>Bright Over Dusk Ltd – Professional Cleaning Service</title>
<link href="https://fonts.googleapis.com/css2?family=Raleway:wght@400;500;600;700&family=Arimo:wght@400;700&display=swap" rel="stylesheet">
<style>
  :root{
    --blue-deep:#0455a3;
    --blue-mid:#3176b5;
    --blue-soft:#85acd3;
    --blue-pale:#cfdeed;
    --white:#ffffff;
    --ink:#1b1b1b;
    --line-grey:#c8c8c8;
    --text-grey:#757575;
  }
  *{margin:0;padding:0;box-sizing:border-box}
  html,body{width:726px;height:1200px;overflow:hidden;background:var(--white)}
  body{font-family:"Arimo",Arial,sans-serif;color:var(--ink);position:relative}
  .page{position:relative;width:726px;height:1200px;overflow:hidden}

  /* hero */
  .hero-photo{position:absolute;left:0;top:0;width:726px;height:420px;
    background:
      radial-gradient(ellipse 180px 120px at 90px 130px,rgba(255,255,255,.95),rgba(255,255,255,0) 100%),
      radial-gradient(ellipse 160px 60px at 120px 300px,rgba(226,222,214,.9),rgba(226,222,214,0) 100%),
      radial-gradient(ellipse 200px 90px at 200px 380px,rgba(200,190,176,.55),rgba(200,190,176,0) 100%),
      radial-gradient(ellipse 220px 150px at 560px 230px,rgba(216,224,232,.85),rgba(216,224,232,0) 100%),
      radial-gradient(ellipse 150px 80px at 640px 60px,rgba(246,247,249,.9),rgba(246,247,249,0) 100%),
      linear-gradient(100deg,#f4f5f6 0%,#ebedee 35%,#e2e6ea 60%,#d9dfe5 85%,#e6eaee 100%)}
  .hero-shape{position:absolute;left:0;top:330px;width:726px;height:100px}
  .main-nav{position:absolute;left:0;top:0;width:726px;height:47px;border-bottom:1px solid rgba(200,200,200,.7)}
  .main-nav a{position:absolute;top:18px;font-family:"Arimo",sans-serif;font-size:11px;color:#2a2a2a;text-decoration:none;letter-spacing:.2px}
  .main-nav a.is-active{color:var(--blue-deep)}
  .nav-underline{position:absolute;left:205px;top:45px;width:46px;height:2px;background:var(--blue-deep)}
  .brand-hero{position:absolute;left:0;top:118px;width:726px;text-align:center}
  .brand-hero .brand-mark{display:inline-block;width:26px;height:26px;border-radius:50%;background:var(--blue-deep);vertical-align:top;margin:20px 14px 0 0}
  .brand-hero .brand-name{display:inline-block;font-family:"Raleway",sans-serif;font-weight:700;font-size:54px;line-height:62px;color:var(--blue-deep);text-align:left;vertical-align:top}

  /* services */
  .section-title{position:absolute;left:0;top:428px;width:726px;text-align:center;font-family:"Raleway",sans-serif;font-weight:400;font-size:26px;color:var(--ink);letter-spacing:.3px}
  .section-title .accent{color:var(--blue-deep)}
  .section-intro{position:absolute;left:90px;top:468px;width:546px;text-align:center;font-size:8.6px;line-height:16.5px;color:var(--text-grey)}
  .service-card{position:absolute;width:142px;text-align:center}
  .service-photo{width:142px;height:91px}
  .service-title{margin-top:10px;font-family:"Raleway",sans-serif;font-weight:500;font-size:15.5px;line-height:19px;color:var(--blue-deep)}
  .service-text{margin-top:4px;margin-left:-6px;width:154px;font-size:8.4px;line-height:16.3px;color:var(--text-grey);white-space:nowrap}

  /* footer */
  .footer-shape{position:absolute;left:0;top:944px;width:726px;height:222px}
  .footer-brand{position:absolute;left:50px;top:1040px;width:140px;font-family:"Raleway",sans-serif;font-weight:700;font-size:21px;line-height:24px;color:var(--blue-deep)}
  .footer-brand .brand-mark{display:inline-block;width:12px;height:12px;border-radius:50%;background:var(--blue-deep);margin-right:6px}
  .footer-col{position:absolute;top:1020px}
  .footer-heading{font-family:"Raleway",sans-serif;font-weight:700;font-size:11.5px;color:var(--blue-deep);letter-spacing:.3px}
  .link-list{list-style:none;margin-top:12px}
  .link-list li{font-size:8.8px;color:#555;height:16.4px;padding-left:13px;position:relative}
  .link-list li::before{content:"";position:absolute;left:0;top:3px;width:5px;height:5px;border:1px solid var(--blue-deep)}
  .link-list li.is-current::before{background:var(--blue-deep)}
  .contact-item{position:relative;padding-left:22px;font-size:8.6px;line-height:16.3px;color:#444}
  .contact-item svg{position:absolute;left:0;top:2px}
  .newsletter-text{margin-top:12px;font-size:8.6px;line-height:13.8px;color:#444;width:150px}
  .email-field{margin-top:7px;width:151px;height:25px;border:1px solid var(--line-grey);background:var(--white);font-size:8.6px;color:#555;padding:8px 6px}
  .submit-btn{margin-top:7px;width:94px;height:25px;background:var(--blue-deep);color:var(--white);font-size:11px;text-align:center;line-height:25px;letter-spacing:.3px}
  .copyright-bar{position:absolute;left:0;top:1165px;width:726px;height:35px;background:var(--blue-deep);text-align:center;line-height:35px;font-size:8.8px;color:var(--blue-pale)}
  .copyright-bar strong{color:var(--white);font-weight:400}
</style>
</head>
<body>
<div class="page">

  <header>
    <div class="hero-photo" role="img" aria-label="Bright, airy interior of a white living room and glass-walled office"></div>
    <svg class="hero-shape" viewBox="0 330 726 100" width="726" height="100" aria-hidden="true">
      <defs>
        <linearGradient id="chevronStroke" x1="0" x2="1" y1="0" y2="0">
          <stop offset="0" stop-color="#0455a3"/>
          <stop offset="0.6" stop-color="#3176b5"/>
          <stop offset="1" stop-color="#cfdeed"/>
        </linearGradient>
      </defs>
      <polygon points="0,416 363,346 726,414 726,430 0,430" fill="#ffffff"/>
      <polyline points="0,416 363,346 726,414" fill="none" stroke="url(#chevronStroke)" stroke-width="5"/>
    </svg>
    <nav class="main-nav">
      <a class="is-active" href="#" style="left:212px">HOME</a>
      <a href="#" style="left:285px">ABOUT US</a>
      <a href="#" style="left:366px">SERVICES</a>
      <a href="#" style="left:446px">BLOG</a>
      <a href="#" style="left:502px">CONTACT US</a>
      <span class="nav-underline"></span>
    </nav>
    <div class="brand-hero"><span class="brand-mark"></span><span class="brand-name">Bright Over<br>Dusk Ltd</span></div>
  </header>

  <main>
    <h1 class="section-title">COMMERCIAL <span class="accent">SERVICES</span></h1>
    <p class="section-intro">Lorem Ipsum is simply dummy text of the printing and typesetting industry. Lorem Ipsum has been the industry's standard dummy text ever since the 1500s, when an unknown printer took a galley of type and scrambled it to make a type specimen book.It has survived not only five centuries Lorem Ipsum is simply dummy text.</p>

    <article class="service-card" style="left:46px;top:534px">
      <div class="service-photo" role="img" aria-label="Clothes iron on white linen" style="background:radial-gradient(ellipse 40px 45px at 55px 40px,#3a3d40,rgba(58,61,64,0) 100%),linear-gradient(180deg,#7d8184 0%,#a7abae 55%,#dfe1e3 80%,#f4f4f5 100%)"></div>
      <h2 class="service-title">Ironing</h2>
      <p class="service-text">Lorem Ipsum is simply dummy text<br>of the printing and typesetting<br>industry. Lorem Ipsum has been...</p>
    </article>
    <article class="service-card" style="left:210px;top:534px">
      <div class="service-photo" role="img" aria-label="Freshly cleaned carpeted living room" style="background:radial-gradient(ellipse 40px 30px at 115px 25px,#f7f7f5,rgba(247,247,245,0) 100%),linear-gradient(180deg,#e4e3df 0%,#d6d5d1 45%,#8d8c88 55%,#bdbcb8 65%,#a6a5a1 100%)"></div>
      <h2 class="service-title">Carpet Cleaning</h2>
      <p class="service-text">Lorem Ipsum is simply dummy text<br>of the printing and typesetting<br>industry. Lorem Ipsum has been...</p>
    </article>
    <article class="service-card" style="left:374px;top:534px">
      <div class="service-photo" role="img" aria-label="Polished wooden floor" style="background:radial-gradient(ellipse 45px 12px at 70px 58px,#f0b43a,rgba(240,180,58,0) 100%),linear-gradient(180deg,#f2e6d8 0%,#ecdac6 55%,#c48755 68%,#a7673a 100%)"></div>
      <h2 class="service-title">Tiled floor steam clean</h2>
      <p class="service-text">Lorem Ipsum is simply dummy text<br>of the printing and typesetting<br>industry. Lorem Ipsum has been...</p>
    </article>
    <article class="service-card" style="left:537px;top:534px">
      <div class="service-photo" role="img" aria-label="Bright white kitchen ready for end of tenancy" style="background:radial-gradient(ellipse 30px 20px at 60px 15px,#8ec9ee,rgba(142,201,238,0) 100%),linear-gradient(135deg,#eef3f6,#f8f9fa 50%,#d7e2ea)"></div>
      <h2 class="service-title">End of tenancy clean</h2>
      <p class="service-text">Lorem Ipsum is simply dummy text<br>of the printing and typesetting<br>industry. Lorem Ipsum has been...</p>
    </article>
    <article class="service-card" style="left:46px;top:742px">
      <div class="service-photo" role="img" aria-label="Home with moving boxes before a house move" style="background:radial-gradient(ellipse 60px 25px at 70px 55px,#e9c3a6,rgba(233,195,166,0) 100%),linear-gradient(180deg,#eee9e3 0%,#dcc6ab 45%,#c9a077 80%,#b98c5f 100%)"></div>
      <h2 class="service-title">New house pre moving in clean</h2>
      <p class="service-text">Lorem Ipsum is simply dummy text<br>of the printing and typesetting<br>industry. Lorem Ipsum has been...</p>
    </article>
    <article class="service-card" style="left:210px;top:742px">
      <div class="service-photo" role="img" aria-label="Cleaning team ready for an emergency call-out" style="background:radial-gradient(ellipse 62px 30px at 71px 46px,#5aa6df,rgba(90,166,223,0) 100%),linear-gradient(180deg,#ffffff 0%,#eef3f8 30%,#dbe7f2 55%,#f2f5f8 80%,#ffffff 100%)"></div>
      <h2 class="service-title">Emergency requested clean</h2>
      <p class="service-text">Lorem Ipsum is simply dummy text<br>of the printing and typesetting<br>industry. Lorem Ipsum has been...</p>
    </article>
  </main>

  <footer>
    <svg class="footer-shape" viewBox="0 944 726 222" width="726" height="222" role="img" aria-label="Soft, light backdrop of a bright clean home">
      <defs>
        <linearGradient id="footerBackdrop" x1="0" x2="1" y1="0" y2="1">
          <stop offset="0" stop-color="#f3f1ee"/>
          <stop offset="0.35" stop-color="#f6ede4"/>
          <stop offset="0.7" stop-color="#f4f3f1"/>
          <stop offset="1" stop-color="#ecebea"/>
        </linearGradient>
      </defs>
      <polygon points="0,1016 363,952 726,1016 726,1166 0,1166" fill="url(#footerBackdrop)"/>
      <polyline points="0,1016 363,952 726,1016" fill="none" stroke="#0455a3" stroke-width="5"/>
    </svg>

    <div class="footer-brand"><span class="brand-mark"></span>Bright<br>Over Dusk<br>Ltd</div>

    <div class="footer-col" style="left:213px">
      <h3 class="footer-heading">USEFULL LINKS</h3>
      <ul class="link-list">
        <li class="is-current">Home</li>
        <li>About Us</li>
        <li>Services</li>
        <li>Blog</li>
        <li>Contact Us</li>
      </ul>
    </div>

    <div class="footer-col" style="left:366px">
      <h3 class="footer-heading" style="margin-left:2px">GET IN TOUCH</h3>
      <div class="contact-item" style="margin-top:11px;width:140px">
        <svg width="14" height="12" viewBox="0 0 14 12" fill="none" stroke="#0455a3" stroke-width="1"><path d="M1 2 L5 1 L9 2 L13 1 V10 L9 11 L5 10 L1 11 Z M5 1 V10 M9 2 V11"/></svg>
        101- Lorem ipsum is simple dummy text of print and type setting industry
      </div>
      <div class="contact-item" style="margin-top:7px">
        <svg width="13" height="13" viewBox="0 0 13 13" fill="none" stroke="#0455a3" stroke-width="1"><path d="M3 1 L5 4 L3.8 5.6 C4.6 7.4 5.6 8.4 7.4 9.2 L9 8 L12 10 L10.6 12 C5.6 11.6 1.4 7.4 1 2.4 Z"/></svg>
        0700 900 3185
      </div>
      <div class="contact-item" style="margin-top:7px">
        <svg width="13" height="11" viewBox="0 0 13 11" fill="none" stroke="#0455a3" stroke-width="1"><rect x="0.5" y="0.5" width="12" height="10"/><path d="M0.5 0.5 L6.5 6 L12.5 0.5"/></svg>
        hello@brightoverdusk.example
      </div>
    </div>

    <div class="footer-col" style="left:529px">
      <h3 class="footer-heading">NEWSLETTER</h3>
      <p class="newsletter-text">Would you like to receive exclusive access to articles, white papers and our regular monthly newsletter?</p>
      <div class="email-field">Enter Email Id</div>
      <div class="submit-btn">SUBMIT</div>
    </div>

    <div class="copyright-bar">© 2016 <strong>Bright Over Dusk</strong> -  All rights reserved.</div>
  </footer>

</div>
</body>
</html>
```